Business card design for engineering firm specializing in defense industry.

We need a professional business card design. Something simple but stands out. We are an engineering company specializing in composites in the defense industry.
Industry/Entity Type
Defense
Contact Information for Business Card
A simple black business card with the Fibrolane yellow color is what we had in mind but open for other designs.
Colors
ffc214

```html
<!DOCTYPE html>
<html lang="en">
<head>
<meta charset="utf-8">
<title>Fibrolane business cards</title>
<link href="https://fonts.googleapis.com/css2?family=Montserrat:wght@400;700&display=swap" rel="stylesheet">
<style>
  :root {
    --brand-yellow: #ffc214;
    --card-dark: #2c2e31;
    --card-light: #f4f4f2;
    --ink: #111111;
    --ink-soft: #333333;
    --backdrop: #5b5b5b;
  }
  html, body {
    margin: 0;
    padding: 0;
    overflow: hidden;
  }
  body {
    width: 1200px;
    height: 900px;
    background: var(--backdrop);
    font-family: "Montserrat", sans-serif;
    position: relative;
  }
  .card {
    position: absolute;
    width: 630px;
    height: 360px;
    box-shadow: 0 18px 40px rgba(0,0,0,0.35);
    overflow: hidden;
  }
  .card--back {
    left: 500px;
    top: 70px;
    background: var(--card-dark);
    display: flex;
    align-items: center;
    justify-content: center;
    gap: 18px;
  }
  .card--front {
    left: 70px;
    top: 470px;
    background: var(--card-light);
  }
  .brand-mark {
    width: 22px;
    height: 22px;
    background: var(--brand-yellow);
  }
  .brand-name {
    font-weight: 700;
    font-size: 52px;
    letter-spacing: 1px;
    color: #ffffff;
  }
  .identity-block {
    position: absolute;
    left: 0;
    top: 0;
    width: 250px;
    height: 360px;
    background: var(--brand-yellow);
    display: flex;
    flex-direction: column;
    justify-content: center;
    padding-left: 40px;
    box-sizing: border-box;
  }
  .person-name {
    font-weight: 700;
    font-size: 26px;
    color: var(--ink);
    margin: 0;
    letter-spacing: 0.5px;
  }
  .person-role {
    font-size: 17px;
    color: var(--ink-soft);
    margin: 4px 0 0 0;
  }
  .front-brand {
    position: absolute;
    left: 300px;
    top: 100px;
    display: flex;
    align-items: center;
    gap: 12px;
  }
  .front-brand .brand-name {
    color: var(--ink);
    font-size: 42px;
  }
  .contact-list {
    position: absolute;
    left: 300px;
    top: 225px;
    list-style: none;
    margin: 0;
    padding: 0;
  }
  .contact-item {
    display: flex;
    align-items: center;
    gap: 14px;
    font-size: 17px;
    color: var(--ink);
    margin-bottom: 10px;
  }
  .contact-icon {
    width: 16px;
    height: 16px;
    flex: none;
  }
</style>
</head>
<body>

<section class="card card--back" aria-label="Card back">
  <span class="brand-mark"></span>
  <span class="brand-name">Fibrolane</span>
</section>

<section class="card card--front" aria-label="Card front">
  <div class="identity-block">
    <p class="person-name">ALEX MARROW</p>
    <p class="person-role">Director</p>
  </div>

  <div class="front-brand">
    <span class="brand-mark"></span>
    <span class="brand-name">Fibrolane</span>
  </div>

  <ul class="contact-list">
    <li class="contact-item">
      <svg class="contact-icon" viewBox="0 0 16 16" aria-hidden="true">
        <path d="M4 1 L6.5 4 L5 6 Q7 10 10 11 L12 9.5 L15 12 L13 15 Q3 14 1 3 Z" fill="#ffc214"/>
      </svg>
      555-014-2270
    </li>
    <li class="contact-item">
      <svg class="contact-icon" viewBox="0 0 16 16" aria-hidden="true">
        <rect x="1" y="3" width="14" height="10" fill="#ffc214"/>
        <path d="M1 3 L8 9 L15 3" fill="none" stroke="#f4f4f2" stroke-width="1.3"/>
      </svg>
      alex.marrow@fibrolane.com
    </li>
    <li class="contact-item">
      <svg class="contact-icon" viewBox="0 0 16 16" aria-hidden="true">
        <circle cx="8" cy="8" r="7" fill="#ffc214"/>
        <path d="M1 8 H15 M8 1 V15 M8 1 Q3 8 8 15 M8 1 Q13 8 8 15" fill="none" stroke="#f4f4f2" stroke-width="1"/>
      </svg>
      www.fibrolane.com
    </li>
  </ul>
</section>

</body>
</html>
```